Web Design Project

We need a web design for a new company that we started called ZARN CNG. ZARN CNG is a company that will build, own and operate compressed natural gas fueling stations throughout the United States. Our primary customers are Trucking companies and the stations will be built for semi trucks. CNG is better for the environment than diesel fuel, and will save trucking companies loads of money. It is also a domestic product which means that it will create American jobs and help America become energy independent. I have attached a logo that we are using. We dont need to stay with this logo persay, but it is what we have for now. We have a video on Vidlo that shows a bit of what we are doing. just search for ZARN CNG. ZARN CNG is a sister company of Holtmark of Arizona,www.hkqvz.example and a nationwide distributor of TRIVEX FUEL, www.trivexfuel.example. We will need links to these sites. Please make any pictures of trucks Holtmark trucks, and please do not use pictures of cabover trucks.

Target Market(s)

The target market are truck drivers and truckers.

Industry/Entity Type

Environment

Requirements
Must have
• Map showing station locations, a page with industry news, a page with a savings calculator (we can code the calculator) Site should have links to

```html
<!DOCTYPE html>
<html lang="en">
<head>
<meta charset="utf-8">
<title>ZARN CNG</title>
<link href="https://fonts.googleapis.com/css2?family=Arimo:wght@400;700&family=Cabin+Sketch:wght@700&display=swap" rel="stylesheet">
<style>
:root{
  --bar:#333333;
  --bar-line:#e6e6e6;
  --page-light:#dedede;
  --page-mid:#c4c4c4;
  --frame:#3a3a3a;
  --panel:#b3b3b3;
  --ink:#111111;
  --ink-soft:#3a3a3a;
  --white:#ffffff;
  --logo:#d9d9d9;
  --divider:#4a4a4a;
  --accent:#1fd39a;
  --dot:#8d8d8d;
}
*{box-sizing:border-box;margin:0;padding:0}
html,body{width:1200px;height:1098px;overflow:hidden}
body{
  position:relative;
  font-family:"Arimo",Arial,sans-serif;
  color:var(--ink);
  background:radial-gradient(ellipse at 50% 45%,var(--page-light) 0%,#d0d0d0 45%,var(--page-mid) 100%);
}
.site-header{
  position:absolute;left:0;top:0;width:1200px;height:131px;
  background:var(--bar);border-bottom:3px solid var(--bar-line);
}
.brand{
  position:absolute;left:152px;top:46px;width:172px;height:56px;
  background:#2c2c2c;display:flex;align-items:center;padding-left:18px;
  font-size:27px;font-weight:700;color:var(--logo);letter-spacing:1px;white-space:nowrap;
}
.main-nav{position:absolute;left:0;top:41px;width:1200px;height:68px;z-index:2}
.main-nav .item{
  position:absolute;top:0;height:68px;padding-left:14px;
  border-left:1px solid var(--divider);
  font-size:19px;color:var(--white);line-height:66px;white-space:nowrap;
}
.main-nav .item.current{border-left:none;padding-left:0;font-weight:700}
.main-nav .item.open{font-weight:700;border-left-color:transparent}
.dropdown{
  position:absolute;left:983px;top:41px;width:121px;height:132px;z-index:1;
  background:var(--bar);padding:50px 0 0 10px;
}
.dropdown li{list-style:none;font-size:14px;color:var(--white);line-height:18.5px;white-space:nowrap}
.hero{
  position:absolute;left:152px;top:178px;width:905px;height:294px;
  background:var(--frame);border-radius:14px;
  box-shadow:0 6px 14px rgba(0,0,0,.25);
}
.hero-panel{
  position:absolute;left:12px;top:11px;width:883px;height:272px;
  background:var(--panel);border-radius:12px;
}
.hero-title{
  position:absolute;right:410px;top:72px;text-align:right;
  font-family:"Cabin Sketch",cursive;font-weight:700;font-variant:small-caps;
  color:var(--ink-soft);line-height:1;white-space:nowrap;
}
.hero-title span{display:block}
.hero-title .l1{font-size:54px;letter-spacing:9px;margin-right:-9px}
.hero-title .l2{font-size:36px;letter-spacing:6px;margin-right:-6px;margin-top:-2px}
.hero-title .l3{font-size:58px;letter-spacing:8px;margin-right:-8px;margin-top:-4px}
.hero-photo{
  position:absolute;left:531px;top:18px;width:333px;height:254px;
  border:7px solid var(--frame);border-radius:12px;
  background:linear-gradient(180deg,#bcd3ea 0%,#e6e8ea 55%,#c9c6bf 100%);
}
.pager{position:absolute;left:557px;top:482px;display:flex;gap:9px}
.pager span{width:16px;height:16px;border-radius:50%;background:radial-gradient(circle at 40% 35%,#bbb,var(--dot))}
.pager span.active{background:radial-gradient(circle at 40% 35%,#8ff3cf,var(--accent))}
.intro{position:absolute;left:187px;top:506px;width:833px}
.intro h1{font-size:20px;font-weight:700;margin-bottom:18px}
.intro p{font-size:13.6px;line-height:16.6px;text-align:justify;margin-bottom:17px}
.gallery{position:absolute;left:188px;top:688px;width:833px;height:154px}
.thumb{
  position:absolute;top:0;height:154px;background:#f4f4f4;
  border:1px solid #ccc;border-radius:8px;padding:4px;
}
.thumb .shot{width:100%;height:100%;border-radius:6px}
.features{position:absolute;top:868px;list-style:none}
.features li{position:relative;font-size:16px;line-height:23px;padding-left:17px;white-space:nowrap}
.features li::before{
  content:"";position:absolute;left:0;top:7px;width:10px;height:10px;border-radius:50%;
  background:radial-gradient(circle at 40% 35%,#b8ffe6,var(--accent) 60%,#0f8a62);
}
.site-footer{
  position:absolute;left:0;top:1046px;width:1200px;height:52px;
  background:var(--bar);border-top:3px solid var(--bar-line);
  color:var(--white);font-size:10px;text-align:center;padding-top:17px;line-height:12px;
}
</style>
</head>
<body>
<header class="site-header">
  <div class="brand">ZARN CNG</div>
</header>
<nav class="main-nav">
  <div class="item current" style="left:397px">Home</div>
  <div class="item" style="left:463px">Location</div>
  <div class="item" style="left:566px">Technology</div>
  <div class="item" style="left:693px">Products</div>
  <div class="item" style="left:795px">Savings Calculator</div>
  <div class="item open" style="left:976px">Company</div>
</nav>
<ul class="dropdown">
  <li>About US</li>
  <li>Contact Us</li>
  <li>Career Options</li>
  <li>Employees</li>
</ul>

<section class="hero">
  <div class="hero-panel">
    <h2 class="hero-title"><span class="l1">Reaching</span><span class="l2">Beyond</span><span class="l3">Boundaries</span></h2>
    <div class="hero-photo" role="img" aria-label="Box truck parked at a CNG fueling station canopy"></div>
  </div>
</section>
<div class="pager"><span></span><span class="active"></span><span></span><span></span></div>

<article class="intro">
  <h1>Lorem Ipsum</h1>
  <p>Lorem ipsum dolor sit amet, vel copiosae salutandi ex. Hinc mazim explicari vis ei, in sonet primis neglegentur sed, mei ne dico conceptam incorrupte. Posse deserunt ut qui, pro solum oportere eu. Ius ei quem splendide.</p>
  <p>Definiebas persequeris vix ea, has congue antiopam iracundia ne. Vis facete invidunt et, alterum eleifend in usu. Est graece molestie ut. An pri altera nominati eloquentiam, pri meis intellegebat an, vix prima labore ad. Nec ne postea virtute similique. Ei iriure dolorem dignissim duo, quo ullum inermis convenire te, elit graeco copiosae est in. Vim te ignota mucius eirmod, sit tantas platonem repudiare eu.</p>
</article>

<section class="gallery">
  <div class="thumb" style="left:0;width:202px"><div class="shot" role="img" aria-label="White box truck on a desert road" style="background:linear-gradient(180deg,#7fa3cf,#dfe3e6 55%,#6d6a66)"></div></div>
  <div class="thumb" style="left:214px;width:198px"><div class="shot" role="img" aria-label="Blue dump truck against a blue sky" style="background:linear-gradient(180deg,#6f93c9,#9fb7da 50%,#5a6170)"></div></div>
  <div class="thumb" style="left:426px;width:197px"><div class="shot" role="img" aria-label="Semi truck with trailer before orange desert cliffs" style="background:linear-gradient(180deg,#d98b2e,#b26a2a 45%,#3b3d4a)"></div></div>
  <div class="thumb" style="left:634px;width:199px"><div class="shot" role="img" aria-label="White box truck on a desert road" style="background:linear-gradient(180deg,#7fa3cf,#dfe3e6 55%,#6d6a66)"></div></div>
</section>

<ul class="features" style="left:270px">
  <li>ARIZONA Owned and Operated</li>
  <li>15 stations in or near Arizona</li>
  <li>STATION designed for semi-trucks</li>
  <li>Reducing a dependence on foriegn oil</li>
</ul>
<ul class="features" style="left:697px">
  <li>ENVIRONMENTALLY Friendly</li>
  <li>LESS expensive than diesel</li>
  <li>FAST, easy-to-use dispensers</li>
  <li>Open 24/7-365 days a year</li>
</ul>

<footer class="site-footer">
  Copyright © 2013 ZARN CNG. Use of website constitutes acceptance of our user agreement and Privacy Policy.<br>
  *Conditions apply please see our payment options.
</footer>
</body>
</html>
```